Bluefinch Painting needs a Website

We need a website built for a Painting company I own, we mainly do residential painting, but don't want to be limited to that.

Need to have estimate request form.
Need pic's of past projects

I like the look of the website for http://www.harborline-painters.example
& "Thistledown Property inspections"

My logo that was designed here on ArtHive on the front page

I would like one of the houses I downloaded as part of the background
of the front page.

Target Market(s)

Home owners

Industry/Entity Type

Painting

Number of Pages Required

1 page

Font styles to use
Serif

Requirements
Must have
• Estimate request form for home owners to fill out -
• Name:
• Phone Number:
• Address:
• E-mail:
• Painting project description:
• And my info to:
• My phone number: (555) 318-7764
• My web address bluefinchpainting.example
Nice to have
• My logo that was designed here on ArtHive

```html
<!DOCTYPE html>
<html lang="en">
<head>
<meta charset="utf-8">
<title>Bluefinch Painting</title>
<link rel="stylesheet" href="https://fonts.googleapis.com/css2?family=Open+Sans:wght@300;400;600;700&family=Roboto+Condensed:wght@700&display=swap">
<style>
:root{
  --blue:#1b5f9f;
  --blue-dark:#154d84;
  --blue-light:#6fa3d4;
  --orange:#c65a26;
  --rust:#b2502a;
  --panel:#dcb7a2;
  --cream:#f3f1ea;
  --ink:#222;
  --text:#333;
  --grey:#8f8f8f;
  --footer:#3d3d3d;
  --white:#fff;
}
*{box-sizing:border-box;margin:0;padding:0}
html,body{width:1200px;height:2264px;overflow:hidden}
body{position:relative;background:var(--white);font-family:"Open Sans",Arial,sans-serif;color:var(--text)}
.abs{position:absolute}

/* header */
.topline{left:0;top:0;width:1200px;height:4px;background:var(--blue)}
.brand{left:155px;top:28px;display:flex;align-items:center;gap:12px}
.brand-mark{width:52px;height:52px;background:var(--blue)}
.brand-name{font-size:34px;font-weight:400;color:var(--blue-dark);letter-spacing:1px}
.socials{display:flex;gap:6px}
.socials span{width:18px;height:18px;border-radius:50%;border:1.5px solid #9ab;display:block}
.header-social{left:942px;top:26px}
.phone{left:868px;top:50px;display:flex;align-items:center;gap:8px;font-size:22px;color:var(--ink)}

/* nav */
.nav{left:0;top:110px;width:1200px;height:50px;background:var(--blue)}
.nav ul{list-style:none;position:absolute;left:158px;top:10px;display:flex;gap:6px}
.nav li{font-size:14px;color:var(--white);padding:6px 14px;text-transform:uppercase}
.nav li.active{background:var(--blue-light)}
.quote-btn{right:160px;top:10px;background:var(--white);color:var(--ink);font-size:13px;font-weight:600;padding:7px 14px 7px 52px;text-transform:uppercase;border-radius:2px}
.quote-btn::before{content:"";position:absolute;left:12px;top:9px;width:28px;height:12px;background:var(--ink);border-radius:2px}

/* hero */
.hero{left:0;top:160px;width:1200px;height:355px;background:linear-gradient(180deg,#a9c7de 0%,#8a8a7c 45%,#6d7a56 75%,#9a9890 100%)}
.hero-caption{left:155px;top:470px;width:885px;height:45px;background:rgba(60,60,60,.55);color:var(--white);font-size:22px;padding:8px 12px;text-transform:uppercase}
.hero-dots{left:975px;top:488px;display:flex;gap:6px}
.hero-dots span{width:8px;height:8px;border-radius:50%;background:rgba(255,255,255,.6)}
.hero-dots span:first-child{background:var(--white)}

/* welcome */
.welcome-title{left:0;top:553px;width:1200px;text-align:center;font-size:27px;font-weight:400;color:var(--ink)}
.welcome-text{left:195px;top:596px;width:810px;text-align:center;font-size:12px;line-height:19px;color:var(--text)}
.btn{display:inline-block;background:var(--blue);color:var(--white);font-size:12px;font-weight:600;text-transform:uppercase;border-radius:2px;text-align:center}
.welcome-btn{left:548px;top:666px;width:104px;height:33px;line-height:33px}

/* services */
.services{left:0;top:740px;width:1200px;height:300px;background:var(--cream)}
.tab{top:740px;width:144px;height:128px;background:var(--white);text-align:center;font-size:17px;color:var(--ink);text-transform:uppercase;padding-top:86px}
.tab svg{position:absolute;left:50%;top:24px;transform:translateX(-50%)}
.tab-active{background:var(--orange);color:var(--white)}
.services-head{left:355px;top:906px;font-size:14px;font-weight:400;color:var(--orange);text-transform:uppercase}
.services-text{left:355px;top:928px;width:688px;font-size:12px;line-height:19px;color:var(--text)}
.notch{left:242px;top:1024px;width:0;height:0;border-left:22px solid transparent;border-right:22px solid transparent;border-bottom:16px solid var(--rust)}

/* feature */
.feature{left:0;top:1040px;width:1200px;height:380px;background:var(--rust)}
.feature-panel{left:158px;top:1085px;width:882px;height:300px;background:var(--panel);border:1px solid #e6c9b8}
.feature-photo{left:175px;top:1104px;width:410px;height:262px;background:linear-gradient(160deg,#e8e2d4 0%,#c9c2b2 55%,#8c4a3a 100%)}
.feature-kicker{left:595px;top:1102px;font-size:30px;font-weight:300;color:var(--ink);line-height:1}
.feature-title{left:593px;top:1128px;font-size:62px;font-weight:300;color:var(--ink);line-height:1}
.feature-text{left:597px;top:1192px;width:432px;font-size:12px;line-height:19px;color:var(--text)}
.feature-btn{left:597px;top:1330px;width:106px;height:33px;line-height:33px}

/* projects */
.projects-title{left:0;top:1452px;width:1200px;text-align:center;font-size:26px;font-weight:400;color:var(--ink);text-transform:uppercase}
.project{top:1498px;width:212px}
.project-photo{width:212px;height:97px}
.project h3{font-size:12px;font-weight:600;color:var(--ink);margin-top:16px;text-transform:uppercase}
.project p{font-size:11.5px;line-height:18px;font-style:italic;color:var(--text);margin-top:3px;height:58px}
.project .btn{width:105px;height:33px;line-height:33px;margin-top:10px}
.project .btn.muted{background:#a8a8a8}
.carousel-arrow{top:1605px}

/* news & contact */
.lower{left:0;top:1775px;width:1200px;height:385px;background:linear-gradient(180deg,#e4e6e8 0%,#eef0f1 40%,#e7e8e9 100%)}
.news-title{left:160px;top:1830px;font-size:22px;font-weight:400;color:var(--ink);text-transform:uppercase}
.news-arrows{left:690px;top:1834px}
.news-item{width:275px;display:flex;gap:10px}
.date{width:32px;flex:none;text-align:center}
.date b{display:block;font-family:"Roboto Condensed",Arial,sans-serif;font-size:24px;line-height:30px;color:var(--ink);background:var(--white)}
.date i{display:block;font-style:normal;font-size:9px;line-height:14px;background:var(--blue);color:var(--white);text-transform:uppercase}
.news-item h4{font-size:11px;font-weight:700;color:var(--ink);text-transform:uppercase}
.news-item h4.link{color:var(--blue)}
.news-item p{font-size:11px;line-height:14px;font-style:italic;color:var(--text);margin-top:2px}
.news-item a{display:block;font-size:11px;font-weight:600;color:var(--blue-dark);text-decoration:none;margin-top:6px;text-transform:uppercase}
.rule{height:1px;background:#cfcfcf}
.contact{left:752px;top:1820px;width:278px;height:312px;background:var(--blue);padding:14px 20px}
.contact h2{font-size:22px;font-weight:400;color:var(--white);text-transform:uppercase;margin-bottom:10px}
.field{display:block;width:100%;height:27px;background:var(--white);border:0;margin-bottom:6px;font-size:11px;font-style:italic;color:#888;padding:6px 8px;font-family:inherit;resize:none}
.field.message{height:56px}
.submit{width:90px;height:28px;line-height:28px;background:var(--blue-light);margin-top:2px}

/* footer */
.footer{left:0;top:2160px;width:1200px;height:104px;background:var(--footer);border-top:4px solid #9a9a9a}
.footer-social{left:555px;top:2190px}
.footer-social span{border-color:#ccc}
.copyright{left:0;top:2226px;width:1200px;text-align:center;font-size:12px;color:#ddd}
.copyright b{color:var(--white)}
</style>
</head>
<body>

<div class="abs topline"></div>

<header>
  <div class="abs brand">
    <span class="brand-mark"></span>
    <span class="brand-name">Bluefinch Painting</span>
  </div>
  <div class="abs socials header-social"><span></span><span></span><span></span><span></span></div>
  <div class="abs phone">
    <svg width="18" height="20" viewBox="0 0 24 24"><path fill="#1b5f9f" d="M6.6 10.8a15 15 0 0 0 6.6 6.6l2.2-2.2c.3-.3.7-.4 1-.2 1.1.4 2.3.6 3.6.6.6 0 1 .4 1 1V20c0 .6-.4 1-1 1A17 17 0 0 1 3 4c0-.6.4-1 1-1h3.5c.6 0 1 .4 1 1 0 1.3.2 2.5.6 3.6.1.3 0 .7-.2 1z"/></svg>
    <span>(555) 318-7764</span>
  </div>
</header>

<nav class="abs nav">
  <ul>
    <li class="active">Home</li>
    <li>About Us</li>
    <li>Services</li>
    <li>Projects</li>
    <li>Contact Us</li>
  </ul>
  <span class="abs quote-btn">Get a Free Quote</span>
</nav>

<section>
  <div class="abs hero" role="img" aria-label="Photo of a two-storey house with a company pickup truck and branded trailer parked in front"></div>
  <div class="abs hero-caption">Create your world with us</div>
  <div class="abs hero-dots"><span></span><span></span><span></span><span></span></div>
</section>

<section>
  <h1 class="abs welcome-title">Welcome to Bluefinch Painting</h1>
  <p class="abs welcome-text">Sed ut perspiciatis unde omnis iste natus error sit voluptatem accudf dgsantium doloremque laudantium, totam rem aperiam, eaque ipsa quae ab illo inventore veritatis et quasi architecto beatae vitae dicta sunt explicabo. Nemo enim ipsam voluptatem quia voluptas sit aspernatur aut odit aut fugit, sed quia cfdonsequ untur magni dolores eos qui ratione voluptatem sequi nesdfciunt. Neque porro quisquam est, qui dolorem.</p>
  <span class="abs btn welcome-btn">Read More</span>
</section>

<section>
  <div class="abs services"></div>
  <div class="abs tab tab-active" style="left:190px">
    <svg width="40" height="38" viewBox="0 0 40 38"><path fill="#fff" d="M20 2 2 18h5v18h10V25h6v11h10V18h5z"/></svg>
    Exterior
  </div>
  <div class="abs tab" style="left:408px">
    <svg width="44" height="40" viewBox="0 0 44 40"><rect x="10" y="4" width="24" height="18" rx="3" fill="#222"/><rect x="2" y="14" width="8" height="18" rx="2" fill="#222"/><rect x="34" y="14" width="8" height="18" rx="2" fill="#222"/><rect x="10" y="24" width="24" height="8" fill="#222"/><rect x="6" y="32" width="3" height="6" fill="#222"/><rect x="35" y="32" width="3" height="6" fill="#222"/></svg>
    Interior
  </div>
  <div class="abs tab" style="left:636px">
    <svg width="46" height="40" viewBox="0 0 46 40"><path fill="#222" d="M23 1 1 17h6v22h32V17h6z"/><g fill="#fff"><rect x="12" y="20" width="6" height="6"/><rect x="20" y="20" width="6" height="6"/><rect x="28" y="20" width="6" height="6"/><rect x="12" y="29" width="6" height="6"/><rect x="28" y="29" width="6" height="6"/><rect x="20" y="29" width="6" height="10"/></g></svg>
    Residential
  </div>
  <div class="abs tab" style="left:860px">
    <svg width="40" height="40" viewBox="0 0 40 40"><rect x="6" y="2" width="20" height="38" fill="#222"/><rect x="26" y="14" width="10" height="26" fill="#222"/><g fill="#fff"><rect x="9" y="6" width="5" height="4"/><rect x="18" y="6" width="5" height="4"/><rect x="9" y="14" width="5" height="4"/><rect x="18" y="14" width="5" height="4"/><rect x="9" y="22" width="5" height="4"/><rect x="18" y="22" width="5" height="4"/><rect x="9" y="30" width="5" height="4"/><rect x="18" y="30" width="5" height="4"/><rect x="29" y="18" width="4" height="4"/><rect x="29" y="26" width="4" height="4"/></g></svg>
    Commercial
  </div>
  <h2 class="abs services-head">Rtis unde omnis iste natus error sit voluptatem</h2>
  <p class="abs services-text">Taccudf dgsantium doloremque laudantium, totam rem aperiam, eaque ipsa quae ab illo inventore veritfjhfghj fjhatis et quasi architecto beatae vitae dicta sunt explicabo. Nemo eniadsfim ipsam voluptatem quia volupt as sit aspef dfgfghfjfvnj natur aut odit aut fudgit, sed quia cfdonsequ untur magni dolores eos qui rasdfasdf asdatione voluptatem sequi nesdfgfdsfjdfci sunt. Neque porro quisquam est, qui dolorem ipsum quia dolor sit amet, consiectetur, adipisci velit, sed quia non numq uam eius modi tempor.</p>
  <div class="abs notch"></div>
</section>

<section>
  <div class="abs feature"></div>
  <div class="abs feature-panel"></div>
  <div class="abs feature-photo" role="img" aria-label="Photo of a painter on a scaffold painting the white trim of a house exterior"></div>
  <div class="abs feature-kicker">EXTERIOR</div>
  <h2 class="abs feature-title">PAINTING</h2>
  <p class="abs feature-text">Sed ut perspiciatis unde omnis iste natus error sit voluptatem accudf dgsantium doloremque laudantium, totam rem aperiam, eaque ipsa quae ab illo inventore veritatis et quasi architecto beatae vitae dicta sunt explicabo. Nemo enim ipsam voluptatem quia voluptas sit aspernatur aut odit aut fugit, sed quia cfdonsequ untur magni dolores eos qui ratione voluptatem sequi nesdfciunt. Neque porro quisquam est, qui dolorem ipsum quia dolor sit amet, consiectetur, adipisci velit, sed quia non numquam eius modi tempor.</p>
  <span class="abs btn feature-btn">Read More</span>
</section>

<section>
  <h2 class="abs projects-title">Our Latest Projects</h2>
  <svg class="abs carousel-arrow" style="left:118px" width="16" height="46" viewBox="0 0 16 46"><path d="M14 2 2 23l12 21" fill="none" stroke="#bbb" stroke-width="2"/></svg>
  <svg class="abs carousel-arrow" style="left:1066px" width="16" height="46" viewBox="0 0 16 46"><path d="M2 2l12 21L2 44" fill="none" stroke="#bbb" stroke-width="2"/></svg>

  <article class="abs project" style="left:155px">
    <div class="project-photo" role="img" aria-label="Photo of a bedroom with red painted walls" style="background:linear-gradient(135deg,#c8323a,#8a2a30 60%,#d9d4cf)"></div>
    <h3>Lorem ipsum dolor sit amet</h3>
    <p>Rodipiscing elit, sed do eiusmod tempr incididunt ut labore et dolore majhkna aliqua. Ut enim ad minim.</p>
    <span class="btn">Read More</span>
  </article>
  <article class="abs project" style="left:382px">
    <div class="project-photo" role="img" aria-label="Black and white photo of a suburban house" style="background:linear-gradient(180deg,#bfbfbf,#7d7d7d 60%,#9a9a9a)"></div>
    <h3>Lorem ipsum dolor sit amet</h3>
    <p>Radipiscing elit, sed do eiusmod tempor incididunt ut labore et dolore majhkna aliqua. Ut enim ad minim.</p>
    <span class="btn muted">Read More</span>
  </article>
  <article class="abs project" style="left:608px">
    <div class="project-photo" role="img" aria-label="Photo of a living room with orange and yellow feature walls" style="background:linear-gradient(90deg,#d8451e,#c83c1c 55%,#e0c21e)"></div>
    <h3>Lorem ipsum dolor sit amet</h3>
    <p>Radipiscing elit, sed do eiusmod incidid unt ut labore et dolore majhkna aliqua. Ut enim ad minim veniam.</p>
    <span class="btn">Read More</span>
  </article>
  <article class="abs project" style="left:834px">
    <div class="project-photo" role="img" aria-label="Photo of a freshly painted single-storey house with a garage" style="background:linear-gradient(180deg,#6e9ed2,#7d8a86 55%,#4f6a3a)"></div>
    <h3>Lorem ipsum dolor sit amet</h3>
    <p>Radipiscing elit, sed do eiusmod tepor incididunt ut labore et dolore majhkna aliqua. Ut enim ad minim.</p>
    <span class="btn">Read More</span>
  </article>
</section>

<section>
  <div class="abs lower" role="img" aria-label="Faint background photo of a house"></div>
  <h2 class="abs news-title">Latest News</h2>
  <svg class="abs news-arrows" width="36" height="18" viewBox="0 0 36 18"><path d="M10 2 3 9l7 7M26 2l7 7-7 7" fill="none" stroke="#999" stroke-width="1.5"/></svg>

  <article class="abs news-item" style="left:160px;top:1876px">
    <div class="date"><b>10</b><i>June</i></div>
    <div><h4>Lorem ipsum dolor sit amet</h4><p>Neque porro quisquam est, qui dolorem ipsum quia dolor sit amet, consdfgs porro quisquam est, qui dolorem</p><a>- Read More</a></div>
  </article>
  <article class="abs news-item" style="left:456px;top:1876px">
    <div class="date"><b style="color:#1b5f9f">15</b><i style="background:#666">June</i></div>
    <div><h4 class="link">Lorem ipsum dolor sit amet</h4><p>Neque porro quisquam est, qui dolorem ipsum quia dolor sit amet, consdfgs porro quisquam est, qui dolorem</p><a style="color:#222">- Read More</a></div>
  </article>
  <div class="abs rule" style="left:160px;top:1978px;width:570px"></div>
  <article class="abs news-item" style="left:160px;top:2012px">
    <div class="date"><b>18</b><i>June</i></div>
    <div><h4>Lorem ipsum dolor sit amet</h4><p>Neque porro quisquam est, qui dolorem ipsum quia dolor sit amet, consdfgs porro quisquam est, qui dolorem</p><a>- Read More</a></div>
  </article>
  <article class="abs news-item" style="left:456px;top:2012px">
    <div class="date"><b>20</b><i>June</i></div>
    <div><h4>Lorem ipsum dolor sit amet</h4><p>Neque porro quisquam est, qui dolorem ipsum quia dolor sit amet, consdfgs porro quisquam est, qui dolorem</p><a>- Read More</a></div>
  </article>

  <form class="abs contact">
    <h2>Quick Contact</h2>
    <input class="field" placeholder="Name">
    <input class="field" placeholder="Mobile">
    <input class="field" placeholder="Address">
    <input class="field" placeholder="E-mail">
    <textarea class="field message" placeholder="Message"></textarea>
    <span class="btn submit">Submit</span>
  </form>
</section>

<footer>
  <div class="abs footer"></div>
  <div class="abs socials footer-social"><span></span><span></span><span></span><span></span></div>
  <p class="abs copyright">© 2015. <b>Bluefinch Painting.</b> All rights reserved.</p>
</footer>

</body>
</html>
```